Veltrona 4", 6", 8" DX pumps catalog

A professional clean looking work.

Please put the file named "Write up" for the full description.

For this project, we want the portrait landscape.
Please based the front and back cover design on the two previous jobs, files marked as “Previous Job 1 and Job 2” It will be appreciated if you can come up with two alternatives for the covers: one design on each previous job design
You are free to change the design a little bit so that it is slightly different from the previous job but not too much so that there are still “similarities” and corporate identity.
For the inserts, you are free to deviate from the two previous jobs.
Colors used bright yellow Pantone 803C and dark grey instead of black.
Wordings are all either black or white, not dark grey
Please design the catalog with CYMCK and not with Pantone.

Project Deadline Extended
Reason: Expect the finalization of at least the front and back cover by 11th of November. 11th to 17th is for the finalization of the inserts Dateline required by the 17th and not 22nd as we need the works to be printed on time for the exhibition

Dear Designers, Please submit your front and back cover designs at the earliest

• Clean, professional look, portrait orientation
• Corporate yellow color and dark grey colours used.
• Wordings in black color
• Design in CYMCK and not in pantone
• Some corporate identity with the previous 2 jobs especially for the front and back cover. For the Inserts - you are free to deviate
• Messy

```html
<!DOCTYPE html>
<html lang="en">
<head>
<meta charset="utf-8">
<title>Veltrona DX Pumps – Value Added Features</title>
<link href="https://fonts.googleapis.com/css2?family=Bebas+Neue&family=Didact+Gothic&display=swap" rel="stylesheet">
<style>
  :root {
    --corporate-yellow: #ffe81f;
    --band-dark-left: #27230f;
    --band-dark-right: #2b2b2b;
    --paper: #ffffff;
    --text-light: #ffffff;
    --text-dark: #000000;
  }
  html, body {
    margin: 0;
    padding: 0;
    overflow: hidden;
  }
  .page {
    position: relative;
    width: 848px;
    height: 1200px;
    background: var(--paper);
    overflow: hidden;
  }
  .yellow-column {
    position: absolute;
    left: 0;
    top: 0;
    width: 435px;
    height: 1200px;
    background: var(--corporate-yellow);
  }
  .feature-band {
    position: absolute;
    left: 0;
    top: 391px;
    width: 848px;
    height: 480px;
    background: var(--band-dark-right);
  }
  .feature-band .band-text-area {
    position: absolute;
    left: 0;
    top: 0;
    width: 435px;
    height: 100%;
    background: var(--band-dark-left);
  }
  .pump-photo {
    position: absolute;
    left: 470px;
    top: 216px;
    width: 294px;
    height: 984px;
    border-radius: 22px 22px 0 0;
    background: linear-gradient(90deg, #5a5a5e 0%, #2a2a2c 8%, #c9ccd2 18%, #7d8088 30%, #e6e8ec 45%, #8a8d94 58%, #d4d6da 70%, #6e7178 84%, #b7babf 94%, #4a4b4f 100%);
  }
  .features {
    position: absolute;
    left: 50px;
    top: 416px;
    width: 340px;
    color: var(--text-light);
  }
  .features h1 {
    margin: 0 0 10px;
    font-family: "Bebas Neue", "Arial Narrow", sans-serif;
    font-weight: 400;
    font-size: 35px;
    line-height: 38px;
    letter-spacing: 0.2px;
  }
  .features p {
    margin: 0 0 20.4px;
    font-family: "Didact Gothic", "Century Gothic", sans-serif;
    font-size: 16.3px;
    line-height: 20.4px;
  }
  .features .lead {
    font-weight: 700;
    -webkit-text-stroke: 0.25px var(--text-light);
  }
  .page-number {
    position: absolute;
    left: 770px;
    top: 1155px;
    font-family: "Didact Gothic", "Century Gothic", sans-serif;
    font-size: 16px;
    color: var(--text-dark);
  }
</style>
</head>
<body>
<div class="page">
  <div class="yellow-column"></div>
  <div class="feature-band"><div class="band-text-area"></div></div>
  <div class="pump-photo" role="img" aria-label="Photograph of a polished stainless steel multistage submersible pump body, shown vertically"></div>

  <section class="features">
    <h1>Value Added Features</h1>
    <p><span class="lead">Powered for continuous operation.</span><br>All ratings are well within the working limits of the motor</p>
    <p><span class="lead">Precision stamped welded stainless steel impeller and diffuser in SS 304.</span> Correct number of welding points on the impeller and diffuser and the sheet thickness to assure the part quality.</p>
    <p><span class="lead">Stainless steel shaft is controlled to the tight tolerance for straightness.</span></p>
    <p><span class="lead">Fluted rubber bearing design for free passage of abrasives.</span></p>
    <p><span class="lead">Built in check valve to safe guard the impellers and diffusers against water hammer.</span></p>
  </section>

  <div class="page-number">03</div>
</div>
</body>
</html>
```